Tri-Fold Brochure Redesign for Floral Preservation Business

I would like to redesign my current tri-fold brouchue that I created myself and have it updated. I would like to keep the same content, color and images, but have it redesigned to look fresher and updated. I'm in the the floral preservation business and work with brides in the wedding inductry. I'm looking for a royal/rustic feel and it should relate to the look and feel of my website www.larkmeadow.com. I have included the Photoshop file I used to create my orginal bouchure.

The only content that has changed is my address which is now;
2847 Birchfall Court, Reston VA 20173

Safe Zone Width - 10.875
Safe Zone Height - 8.375

I have included the Photoshop and Illustrator templates for the tri-fold brochure from the printer I will be using.

```html
<!DOCTYPE html>
<html lang="en">
<head>
<meta charset="utf-8">
<title>Lark &amp; Meadow – Tri-Fold Brochure</title>
<link rel="stylesheet" href="https://fonts.googleapis.com/css2?family=Cinzel:wght@400;600&family=Arimo:wght@400;700&family=Pinyon+Script&display=swap">
<style>
  :root {
    --paper: #ffffff;
    --blush: #f8e6ee;
    --blush-deep: #f1d3e0;
    --rose: #d9336f;
    --magenta: #c42a6a;
    --charcoal: #3b3b3b;
    --grey: #595959;
    --logo-red: #c8202f;
    --link-blue: #3b5a9a;
    --frame-line: #9a9a9a;
  }
  * { box-sizing: border-box; margin: 0; padding: 0; }
  html, body { width: 900px; height: 1200px; overflow: hidden; background: var(--paper); }
  body { font-family: "Arimo", Arial, sans-serif; color: var(--charcoal); position: relative; }

  .sheet {
    position: absolute; left: 10px; width: 880px; overflow: hidden;
    background: radial-gradient(ellipse at 70% 40%, var(--blush) 0%, var(--blush-deep) 100%);
  }
  .sheet--outside { top: 25px; height: 570px; }
  .sheet--inside { top: 610px; height: 565px; }

  .abs { position: absolute; }
  .body-copy { font-size: 10.6px; line-height: 13.2px; color: var(--charcoal); }
  .body-copy p + p { margin-top: 13px; }

  .brand {
    display: flex; align-items: center; justify-content: center; gap: 6px;
    font-family: "Cinzel", serif; color: var(--grey); font-weight: 400;
    white-space: nowrap; line-height: 1;
  }
  .brand__mark { background: var(--logo-red); flex: none; }

  .section-title {
    font-family: "Cinzel", serif; font-weight: 600; color: var(--rose);
    font-size: 15px; letter-spacing: .5px; text-align: center; white-space: nowrap;
  }
  .rule { height: 1px; background: var(--rose); opacity: .7; }

  .appointment { font-size: 9.5px; color: var(--rose); text-align: center; letter-spacing: .2px; }
  .address { font-size: 10.6px; line-height: 13px; text-align: center; color: var(--charcoal); white-space: nowrap; }

  .signature { font-family: "Pinyon Script", cursive; font-size: 19px; color: var(--charcoal); }

  .social { display: flex; gap: 8px; align-items: flex-start; }
  .social__icon { width: 34px; height: 32px; background: var(--link-blue); flex: none; }
  .social__text { font-size: 10px; font-weight: 700; color: var(--link-blue); line-height: 13px; }

  .tagline { font-family: "Cinzel", serif; font-size: 10.5px; letter-spacing: .6px; color: var(--charcoal); text-align: center; line-height: 13px; white-space: nowrap; }

  .banner {
    background: var(--magenta); color: #fff;
    font-family: "Cinzel", serif; font-size: 11.2px; letter-spacing: 1px;
    text-align: center; line-height: 13.5px; padding-top: 5px; white-space: nowrap;
  }
  .photo-frame { background: #fff; border: 1px solid var(--frame-line); }
  .photo-fill { position: absolute; }

  .step-script { font-family: "Pinyon Script", cursive; font-size: 24px; text-align: center; color: var(--charcoal); }
  .step-title { font-family: "Cinzel", serif; font-size: 10.5px; color: var(--rose); text-align: center; letter-spacing: .5px; font-weight: 600; }
  .note { font-size: 8.2px; line-height: 10px; text-align: center; color: var(--charcoal); }
</style>
</head>
<body>

<!-- Outside spread -->
<section class="sheet sheet--outside">
  <!-- Panel: About -->
  <div class="brand abs" style="left:55px; top:96px; width:200px; font-size:16px;">
    <span class="brand__mark" style="width:14px;height:14px;"></span>Lark &amp; Meadow
  </div>
  <h2 class="section-title abs" style="left:60px; top:132px; width:170px;">About Us</h2>
  <div class="rule abs" style="left:85px; top:162px; width:150px;"></div>
  <div class="body-copy abs" style="left:26px; top:180px; width:236px;">
    <p>With a rich family history in the floral business spanning over 60 years, I have spent the past two decades learning all aspects of the business but focusing primarily on perfecting the freeze-dry floral preservation process. Most recently I have expanded beyond the conventional freeze-dry offerings and have learned the art of creating flower petal jewelry from preserved flowers. I'm proud to be one of the few companies in the U.S. to offer this unique service.</p>
    <p>At Lark &amp; Meadow, we are committed to being the premiere floral preservation company in your community. I am extremely proud and honored to carry on the family name in the floral business by providing these services not only in my hometown of Washington DC but also in the Hampton Roads metro area. I'm confident the services offered by Lark &amp; Meadow are sure to exceed your expectations for years to come.</p>
  </div>
  <div class="signature abs" style="left:26px; top:462px;">Evan Hollis</div>
  <div class="body-copy abs" style="left:26px; top:502px; width:200px;">Owner &amp; Operator<br>Lark &amp; Meadow</div>

  <!-- Panel: Back -->
  <div class="social abs" style="left:348px; top:127px; width:200px;">
    <span class="social__icon" aria-hidden="true"></span>
    <span class="social__text">Become a fan and view<br>our most recent work</span>
  </div>
  <div class="social__text abs" style="left:330px; top:164px; width:220px; text-align:center;">www.socialpage.com/larkmeadow</div>

  <div class="brand abs" style="left:335px; top:456px; width:200px; font-size:16px;">
    <span class="brand__mark" style="width:14px;height:14px;"></span>Lark &amp; Meadow
  </div>
  <div class="appointment abs" style="left:320px; top:494px; width:230px;">BY APPOINTMENT ONLY</div>
  <div class="address abs" style="left:305px; top:518px; width:260px;">2847 Birchfall Court, Reston VA 20173<br>703.555.0148 | www.larkmeadow.com</div>

  <!-- Panel: Cover -->
  <div class="brand abs" style="left:600px; top:170px; width:280px; font-size:24px; gap:10px;">
    <span class="brand__mark" style="width:26px;height:26px;"></span>Lark &amp; Meadow
  </div>
  <div class="tagline abs" style="left:600px; top:224px; width:270px;">The National Capital's Premier<br>Flower Preservation Professionals</div>
  <div class="appointment abs" style="left:620px; top:494px; width:230px;">BY APPOINTMENT ONLY</div>
  <div class="address abs" style="left:605px; top:518px; width:260px;">2847 Birchfall Court, Reston VA 20173<br>703.555.0148 | www.larkmeadow.com</div>
</section>

<!-- Inside spread -->
<section class="sheet sheet--inside">
  <div class="banner abs" style="left:32px; top:18px; width:530px; height:54px;">
    You Have Chosen The Perfect Flowers. Now Choose The Perfect<br>Way To Cherish Them. Lark &amp; Meadow's Floral Preservation Process<br>Transforms Your Flowers Into Lasting Works of Art or Jewelry
  </div>

  <div class="photo-frame abs" style="left:32px; top:88px; width:240px; height:233px;">
    <div class="photo-fill" role="img" aria-label="Preserved bridal bouquet mounted in a dark wood shadowbox frame" style="left:18px; top:16px; width:204px; height:200px; background:linear-gradient(#6b2a22,#4a1c17); padding:12px;">
      <div style="width:100%;height:100%;background:radial-gradient(circle at 50% 45%, #f4ead8 0%, #e8dcc2 100%);"></div>
    </div>
  </div>
  <div class="photo-frame abs" style="left:322px; top:88px; width:240px; height:233px;">
    <div class="photo-fill" role="img" aria-label="Bracelet of blue flower-petal beads with silver findings" style="left:30px; top:60px; width:180px; height:120px; border-radius:50%; background:radial-gradient(ellipse, #ffffff 35%, #7fb6dc 55%, #ffffff 75%);"></div>
  </div>

  <h2 class="section-title abs" style="left:32px; top:337px; width:240px;">Floral Preservation</h2>
  <div class="rule abs" style="left:72px; top:366px; width:165px;"></div>
  <div class="body-copy abs" style="left:33px; top:385px; width:240px;">
    Our handcrafted shadowboxes are made with the industries finest raw materials to ensure the highest level of quality. We exclusively offer Hartwell-Crane moulding, makers of beautiful moulding for over 100 years. Using archival standards set by the National Archival Board, our shadowboxes are matted and mounted with the Ashford ArchivalGuard system. This system is used by museums to protect some of this nation's most valuable artwork. We finish by using ClearVista's Gallery glass to enhance, protect and beautify. Each of these details contributes to a museum-quality work of art.
  </div>

  <h2 class="section-title abs" style="left:322px; top:337px; width:240px;">Flower-Petal Jewelry</h2>
  <div class="rule abs" style="left:362px; top:366px; width:165px;"></div>
  <div class="body-copy abs" style="left:322px; top:385px; width:236px;">
    If you would like to turn your memories into a wearable story, consider creating signature jewelry. We turn real petals from your blooms into one-of-a-kind jewelry pieces for you or your loved ones. We can transform your flowers into earrings, necklaces, bracelets, Charmwell- and Linkbead-type charms or rosaries. The tradition hails from the historical practice of nuns creating rosaries from condensed flower petals. In that same vein, we create unique pieces to fit your own style. Each piece is made by hand from your flowers and the highest quality sterling silver findings.
  </div>

  <!-- Process panel -->
  <h2 class="section-title abs" style="left:618px; top:16px; width:240px;">The Process</h2>
  <div class="rule abs" style="left:640px; top:42px; width:200px;"></div>
  <div class="step-script abs" style="left:618px; top:48px; width:240px;">Step 1</div>
  <div class="step-title abs" style="left:618px; top:84px; width:240px;">Reserve The Date</div>
  <div class="body-copy abs" style="left:617px; top:101px; width:226px;">
    To ensure our services, you will need to "reserve the date" with a deposit. We accept no more than 4 clients a week and with over 50,000 weddings in the DC and Hampton Roads Metro areas annually, many brides reserve their wedding date up to four months in advance. The full deposit is applied to the cost of your final design selection.
  </div>
  <div class="rule abs" style="left:640px; top:216px; width:200px;"></div>
  <div class="step-script abs" style="left:618px; top:226px; width:240px;">Step 2</div>
  <div class="step-title abs" style="left:618px; top:263px; width:240px;">Secure The Flowers</div>
  <div class="body-copy abs" style="left:617px; top:280px; width:226px;">
    You can either drop your flowers off shortly after the event, or we can pick them up the night of the reception. Is your event out of town? No problem. You can ship them to us overnight or drop them off upon your return.
  </div>
  <div class="rule abs" style="left:640px; top:360px; width:200px;"></div>
  <div class="step-script abs" style="left:618px; top:372px; width:240px;">Step 3</div>
  <div class="step-title abs" style="left:618px; top:411px; width:240px;">Design Selection</div>
  <div class="body-copy abs" style="left:617px; top:428px; width:236px;">
    Within 30 days after your event we ask that you make an appointment to visit our showroom to make your final design selection. Once your order has been placed, it takes approximately 2 to 3 months to complete.
  </div>
  <div class="rule abs" style="left:655px; top:506px; width:170px;"></div>
  <div class="note abs" style="left:630px; top:516px; width:220px;">
    Please visit our website for full details,<br>pricing and additional pictures.<br>www.larkmeadow.com
  </div>
</section>

</body>
</html>
```